Networking card

I just need a simple design with the following information:
Ravin Doshu
318.647.2094
rdoshu583016@mailvanta.com

I would like to have a white background with blue text like in this sample: https://cardmintly.com/business-card-207346/

```html
<!DOCTYPE html>
<html lang="en">
<head>
<meta charset="utf-8">
<title>Ravin Doshu – Networking Card</title>
<link rel="stylesheet" href="https://fonts.googleapis.com/css2?family=Montserrat:wght@400;700&display=swap">
<style>
  :root {
    --page-bg: #9a9a9a;
    --card-bg: #083a5e;
    --card-ink: #ffffff;
    --divider: rgba(255, 255, 255, 0.55);
  }
  html, body {
    margin: 0;
    padding: 0;
    width: 1200px;
    height: 1059px;
    overflow: hidden;
    background: var(--page-bg);
  }
  .canvas {
    position: relative;
    width: 1200px;
    height: 1059px;
  }
  .card {
    position: absolute;
    left: 235px;
    top: 322px;
    width: 729px;
    height: 415px;
    border-radius: 24px;
    background: var(--card-bg);
    color: var(--card-ink);
    font-family: "Montserrat", sans-serif;
  }
  .card-name {
    position: absolute;
    left: 0;
    right: 0;
    top: 134px;
    margin: 0;
    text-align: center;
    font-weight: 700;
    font-size: 42px;
    letter-spacing: 0.5px;
    line-height: 1;
  }
  .card-divider {
    position: absolute;
    left: 341px;
    top: 192px;
    width: 48px;
    height: 1px;
    background: linear-gradient(to right, transparent, var(--divider), transparent);
  }
  .contact {
    position: absolute;
    left: 0;
    right: 0;
    display: flex;
    justify-content: center;
    align-items: center;
    gap: 10px;
    font-weight: 400;
    font-size: 24px;
    line-height: 1;
    letter-spacing: 0.3px;
  }
  .contact-phone { top: 215px; }
  .contact-email { top: 256px; }
  .contact-icon { fill: var(--card-ink); flex: none; }
</style>
</head>
<body>
<div class="canvas">
  <section class="card">
    <h1 class="card-name">RAVIN DOSHU</h1>
    <div class="card-divider"></div>
    <div class="contact contact-phone">
      <svg class="contact-icon" width="20" height="20" viewBox="0 0 24 24" aria-hidden="true">
        <path d="M6.6 10.8a15.1 15.1 0 0 0 6.6 6.6l2.2-2.2a1 1 0 0 1 1-.25 11.4 11.4 0 0 0 3.6.6 1 1 0 0 1 1 1V20a1 1 0 0 1-1 1A17 17 0 0 1 3 4a1 1 0 0 1 1-1h3.5a1 1 0 0 1 1 1c0 1.25.2 2.45.6 3.6a1 1 0 0 1-.25 1z"/>
      </svg>
      <span>318.647.2094</span>
    </div>
    <div class="contact contact-email">
      <svg class="contact-icon" width="20" height="15" viewBox="0 0 20 15" aria-hidden="true">
        <path d="M0 0h20v15H0z" fill="none"/>
        <path d="M0 0l10 8 10-8z M0 2v13l7-7z M20 2v13l-7-7z M8 9l2 1.6L12 9l7 6H1z"/>
      </svg>
      <span>rdoshu583016@mailvanta.com</span>
    </div>
  </section>
</div>
</body>
</html>
```